Business Management Fortress

Assist with enhancing a powerpoint slide by providing a few design options for consideration. I have a template but open to any creative ideas.

Target Market(s)

Internal employees and stakeholders

Industry/Entity Type

Business Management, Finance, Accounting

Requirements
Must have
• Maintain a fortress, temple, or pyramid schema
Nice to have
• Scenic Background

```html
<!DOCTYPE html>
<html lang="en">
<head>
<meta charset="utf-8">
<title>Fiduciary Responsibilities</title>
<link href="https://fonts.googleapis.com/css2?family=Manrope:wght@400;500;600;700;800&display=swap" rel="stylesheet">
<style>
  :root{
    --ink:#0b0b0c;
    --blue:#4a9af5;
    --orange:#f6ad38;
    --green:#3dbf84;
    --red:#f2314f;
    --stone:#dbe3f3;
    --stone-dark:#b9c8e8;
    --white:#ffffff;
  }
  *{margin:0;padding:0;box-sizing:border-box}
  html,body{width:1200px;height:675px;overflow:hidden;background:var(--white)}
  body{font-family:"Manrope",sans-serif;color:var(--ink)}
  .slide{position:relative;width:1200px;height:675px;overflow:hidden}
  .intro{position:absolute;left:55px;top:56px;width:500px}
  .intro__title{font-weight:800;font-size:48px;line-height:47px;letter-spacing:-0.5px}
  .intro__title span{display:block}
  .intro__title .accent{color:var(--blue)}
  .intro__rule{width:109px;height:5px;background:var(--stone);margin-top:16px}
  .intro__text{margin-top:34px;font-size:16.3px;line-height:22.6px;font-weight:500;width:490px}
  .pillars-list{position:absolute;left:55px;top:302px;list-style:none}
  .pillars-list li{display:flex;align-items:center;height:46.5px;font-size:29px;font-weight:500}
  .pillars-list svg{width:28px;height:32px;margin-right:17px}
  .temple{position:absolute;left:0;top:0;width:1200px;height:675px}
  .temple text{font-family:"Manrope",sans-serif}
</style>
</head>
<body>
<main class="slide">
  <section class="intro">
    <h1 class="intro__title"><span>Fiduciary</span><span class="accent">Responsibilities</span></h1>
    <div class="intro__rule"></div>
    <p class="intro__text">Fiduciary responsibilities involve acting in another's best interests with trust, loyalty, and care, prioritizing their needs over one's own.</p>
  </section>

  <ul class="pillars-list">
    <li><svg viewBox="0 0 28 32"><path d="M2 2 L27 16 L2 30 Z" fill="var(--blue)" stroke="var(--blue)" stroke-width="3" stroke-linejoin="round"/></svg>People</li>
    <li><svg viewBox="0 0 28 32"><path d="M2 2 L27 16 L2 30 Z" fill="var(--orange)" stroke="var(--orange)" stroke-width="3" stroke-linejoin="round"/></svg>Innovation</li>
    <li><svg viewBox="0 0 28 32"><path d="M2 2 L27 16 L2 30 Z" fill="var(--green)" stroke="var(--green)" stroke-width="3" stroke-linejoin="round"/></svg>Business Intelligence</li>
    <li><svg viewBox="0 0 28 32"><path d="M2 2 L27 16 L2 30 Z" fill="var(--red)" stroke="var(--red)" stroke-width="3" stroke-linejoin="round"/></svg>Strategic Alliances</li>
  </ul>

  <svg class="temple" viewBox="0 0 2560 1440" aria-label="Temple of fiduciary responsibilities">
    <!-- roof -->
    <path class="roof" d="M1318 442 L1855 226 Q1875 218 1895 226 L2432 442 Q2455 456 2440 472 L1312 472 Q1296 456 1318 442 Z" fill="var(--stone)"/>
    <line x1="1662" y1="298" x2="1838" y2="472" stroke="var(--white)" stroke-width="14"/>
    <line x1="2088" y1="298" x2="1912" y2="472" stroke="var(--white)" stroke-width="14"/>
    <rect class="architrave" x="1355" y="474" width="1042" height="54" rx="22" fill="var(--stone)"/>
    <rect x="1355" y="474" width="1042" height="16" fill="var(--stone-dark)"/>

    <!-- roof callouts -->
    <text x="1355" y="265" font-size="37" font-weight="500" fill="var(--orange)">Leaders</text>
    <path d="M1507 255 H1595 Q1630 255 1630 290 V332" fill="none" stroke="var(--ink)" stroke-width="2.5"/>
    <text x="1875" y="168" font-size="37" font-weight="500" fill="var(--blue)" text-anchor="middle">Partner</text>
    <line x1="1875" y1="188" x2="1875" y2="284" stroke="var(--ink)" stroke-width="2.5"/>
    <text x="2265" y="265" font-size="37" font-weight="500" fill="var(--green)">Profitability</text>
    <path d="M2245 255 H2157 Q2122 255 2122 290 V332" fill="none" stroke="var(--ink)" stroke-width="2.5"/>

    <circle cx="1630" cy="398" r="64" fill="var(--white)"/>
    <circle cx="1875" cy="348" r="64" fill="var(--white)"/>
    <circle cx="2120" cy="398" r="64" fill="var(--white)"/>
    <circle cx="1630" cy="332" r="6" fill="var(--ink)"/>
    <circle cx="1875" cy="284" r="6" fill="var(--ink)"/>
    <circle cx="2122" cy="332" r="6" fill="var(--ink)"/>

    <!-- leaders icon -->
    <g class="icon-leaders" fill="var(--orange)">
      <circle cx="1630" cy="372" r="7"/>
      <rect x="1621" y="382" width="18" height="52" rx="6"/>
      <circle cx="1604" cy="380" r="6"/>
      <rect x="1596" y="389" width="16" height="38" rx="5"/>
      <circle cx="1656" cy="380" r="6"/>
      <rect x="1648" y="389" width="16" height="38" rx="5"/>
      <path d="M1616 355 l4 8 M1630 350 v9 M1644 355 l-4 8" stroke="var(--orange)" stroke-width="3"/>
    </g>
    <!-- handshake icon -->
    <g class="icon-handshake" fill="var(--blue)">
      <path d="M1826 330 l18 -8 l14 34 l-18 8 Z"/>
      <path d="M1924 330 l-18 -8 l-14 34 l18 8 Z"/>
      <path d="M1848 340 q27 -12 54 0 l-8 26 q-20 14 -38 2 Z"/>
    </g>
    <!-- money icon -->
    <g class="icon-money">
      <circle cx="2128" cy="390" r="22" fill="var(--green)"/>
      <rect x="2120" y="358" width="16" height="10" rx="3" fill="var(--green)"/>
      <text x="2128" y="400" font-size="26" font-weight="700" fill="var(--white)" text-anchor="middle">$</text>
      <path d="M2082 428 l22 -22 q10 -8 24 -2 l26 4 l-20 22 h-28 l-12 12 Z" fill="var(--green)"/>
    </g>

    <!-- columns -->
    <g class="columns">
      <g transform="translate(1487 0)">
        <rect x="-70" y="552" width="140" height="29" rx="12" fill="var(--stone)"/>
        <path d="M-47 581 H47 Q62 680 67 770 V930 Q60 1020 50 1113 H-50 Q-60 1020 -67 930 V770 Q-62 680 -47 581 Z" fill="var(--stone)"/>
        <rect x="-70" y="1113" width="140" height="29" rx="12" fill="var(--stone)"/>
        <circle cx="0" cy="858" r="104" fill="var(--stone-dark)"/>
        <circle cx="0" cy="847" r="104" fill="var(--stone)"/>
        <circle cx="0" cy="847" r="79" fill="var(--blue)"/>
        <g fill="var(--white)">
          <circle cx="-28" cy="830" r="13"/><circle cx="28" cy="830" r="13"/><circle cx="0" cy="824" r="15"/>
          <path d="M-46 868 q0 -22 18 -22 q18 0 18 22 Z"/><path d="M10 868 q0 -22 18 -22 q18 0 18 22 Z"/>
          <path d="M-24 884 q0 -40 24 -40 q24 0 24 40 Z"/>
        </g>
      </g>
      <g transform="translate(1746 0)">
        <rect x="-70" y="552" width="140" height="29" rx="12" fill="var(--stone)"/>
        <path d="M-47 581 H47 Q62 680 67 770 V930 Q60 1020 50 1113 H-50 Q-60 1020 -67 930 V770 Q-62 680 -47 581 Z" fill="var(--stone)"/>
        <rect x="-70" y="1113" width="140" height="29" rx="12" fill="var(--stone)"/>
        <circle cx="0" cy="858" r="104" fill="var(--stone-dark)"/>
        <circle cx="0" cy="847" r="104" fill="var(--stone)"/>
        <circle cx="0" cy="847" r="79" fill="var(--orange)"/>
        <g fill="var(--white)">
          <path d="M0 800 q-38 0 -38 40 q0 20 16 34 v14 h44 v-14 q16 -14 16 -34 q0 -40 -38 -40 Z"/>
          <rect x="-16" y="894" width="32" height="6" rx="3"/>
          <rect x="-12" y="904" width="24" height="6" rx="3"/>
        </g>
        <circle cx="12" cy="840" r="10" fill="var(--orange)"/>
      </g>
      <g transform="translate(2005 0)">
        <rect x="-70" y="552" width="140" height="29" rx="12" fill="var(--stone)"/>
        <path d="M-47 581 H47 Q62 680 67 770 V930 Q60 1020 50 1113 H-50 Q-60 1020 -67 930 V770 Q-62 680 -47 581 Z" fill="var(--stone)"/>
        <rect x="-70" y="1113" width="140" height="29" rx="12" fill="var(--stone)"/>
        <circle cx="0" cy="858" r="104" fill="var(--stone-dark)"/>
        <circle cx="0" cy="847" r="104" fill="var(--stone)"/>
        <circle cx="0" cy="847" r="79" fill="var(--green)" role="img" aria-label="Brain with circuit lines icon"/>
      </g>
      <g transform="translate(2264 0)">
        <rect x="-70" y="552" width="140" height="29" rx="12" fill="var(--stone)"/>
        <path d="M-47 581 H47 Q62 680 67 770 V930 Q60 1020 50 1113 H-50 Q-60 1020 -67 930 V770 Q-62 680 -47 581 Z" fill="var(--stone)"/>
        <rect x="-70" y="1113" width="140" height="29" rx="12" fill="var(--stone)"/>
        <circle cx="0" cy="858" r="104" fill="var(--stone-dark)"/>
        <circle cx="0" cy="847" r="104" fill="var(--stone)"/>
        <circle cx="0" cy="847" r="79" fill="var(--red)" role="img" aria-label="Chess knight above handshake icon"/>
      </g>
    </g>

    <!-- base -->
    <rect class="base-top" x="1375" y="1163" width="1002" height="110" rx="26" fill="var(--stone)"/>
    <rect class="base-bottom" x="1300" y="1217" width="1150" height="124" rx="24" fill="var(--stone)"/>
    <text x="1875" y="1211" font-size="30" font-weight="700" fill="var(--ink)" text-anchor="middle">Fiduciary Responsibilities</text>
    <g class="tags" font-size="22" font-weight="500" fill="var(--blue)" text-anchor="middle">
      <rect x="1543" y="1240" width="226" height="36" rx="10" fill="var(--white)"/><text x="1656" y="1266">Accurate Financials</text>
      <rect x="1784" y="1240" width="203" height="36" rx="10" fill="var(--white)"/><text x="1885" y="1266">Internal Controls</text>
      <rect x="2002" y="1240" width="205" height="36" rx="10" fill="var(--white)"/><text x="2104" y="1266">Brand Protection</text>
      <rect x="1634" y="1291" width="147" height="36" rx="10" fill="var(--white)"/><text x="1707" y="1317">Compliance</text>
      <rect x="1796" y="1291" width="87" height="36" rx="10" fill="var(--white)"/><text x="1839" y="1317">Ethics</text>
      <rect x="1898" y="1291" width="217" height="36" rx="10" fill="var(--white)"/><text x="2006" y="1317">Cost Management</text>
    </g>
  </svg>
</main>
</body>
</html>
```